Business Card Design Project for New Home Builder

Double sided card,
Larger logo on 1 side with small quote, Its not just a house, Its your Home, across the bottom. Matt Red base, White logo, black quote??

other side, ,
Its your Home LHS. Smaller logo RHS with.
Details below.

"neuropolitical Rg" Logo Font

Dennis Orford

PO Box 8437 Mildura VIC 3502
Mobile 0427 318865 / Phone 03 50718 962 / Fax 03 50718 415
email DennisO@tbvbuild.net.au
Vic Building Practitioner DB-U 8174 Vic Commercial Builder CB-U 5093
NSW Contractor Reg 37086C

Target Market(s)

New Home Buyers

Industry/Entity Type

Business

Requirements
Must have
• Sharp detail, Red Black & White colourings.
Should not have
• Any new colours

```html
<!DOCTYPE html>
<html lang="en">
<head>
<meta charset="utf-8">
<title>Dennis Orford Homes – Business Card Front</title>
<link rel="stylesheet" href="https://fonts.googleapis.com/css2?family=Anton&display=swap">
<style>
  :root {
    --card-red: #ed1c24;
    --logo-white: #ffffff;
    --quote-black: #231f20;
    --paper: #ffffff;
    --crop-line: #000000;
  }
  html, body {
    margin: 0;
    padding: 0;
    width: 1200px;
    height: 799px;
    overflow: hidden;
    background: var(--paper);
  }
  .sheet {
    position: relative;
    width: 1200px;
    height: 799px;
    background: var(--paper);
  }
  .crop-marks {
    position: absolute;
    inset: 0;
    width: 1200px;
    height: 799px;
  }
  .crop-marks line {
    stroke: var(--crop-line);
    stroke-width: 1;
  }
  .card-face {
    position: absolute;
    left: 26px;
    top: 26px;
    width: 1148px;
    height: 747px;
    background: var(--card-red);
  }
  .brand {
    position: absolute;
    left: 0;
    right: 0;
    top: 218px;
    height: 260px;
    display: flex;
    flex-direction: column;
    align-items: center;
    justify-content: center;
    gap: 36px;
  }
  .brand-mark {
    width: 60px;
    height: 60px;
    background: var(--logo-white);
  }
  .brand-name {
    margin: 0;
    width: 966px;
    text-align: center;
    font-family: "Anton", sans-serif;
    font-weight: 400;
    font-size: 96px;
    line-height: 1;
    letter-spacing: 8px;
    text-transform: uppercase;
    white-space: nowrap;
    color: var(--logo-white);
  }
  .tagline {
    position: absolute;
    left: 0;
    right: 0;
    top: 580px;
    margin: 0;
    text-align: center;
    font-family: "Anton", sans-serif;
    font-weight: 400;
    font-size: 42px;
    line-height: 1;
    letter-spacing: 4px;
    color: var(--quote-black);
  }
</style>
</head>
<body>
  <div class="sheet">
    <section class="card-face">
      <div class="brand">
        <div class="brand-mark"></div>
        <h1 class="brand-name">Dennis Orford Homes</h1>
      </div>
      <p class="tagline">Its not just a house, Its your Home</p>
    </section>

    <svg class="crop-marks" viewBox="0 0 1200 799" aria-hidden="true">
      <line x1="84" y1="0" x2="84" y2="61"/>
      <line x1="1114" y1="0" x2="1114" y2="61"/>
      <line x1="0" y1="84" x2="61" y2="84"/>
      <line x1="1140" y1="84" x2="1200" y2="84"/>
      <line x1="84" y1="738" x2="84" y2="799"/>
      <line x1="1114" y1="738" x2="1114" y2="799"/>
      <line x1="0" y1="712" x2="61" y2="712"/>
      <line x1="1140" y1="712" x2="1200" y2="712"/>
    </svg>
  </div>
</body>
</html>
```